Kitchen and custom cabinetry company looking for business card design

We make: * Custom Kitchens, contemporary and traditional kitchens, Vanities, Libraries, Custom Entry Doors, Custom Wine Cellars and Custom Design Furniture. Phone number 555-271-4486. Address: Westhampton NY. Email: TOLVANE@mailbox-example.com Portfolio at: TOLVANEcabinetry.example I would like moderns fonts and not heavy lines. double side but maybe will use clear plastic. I attached the logo.

```html
<!DOCTYPE html>
<html lang="en">
<head>
<meta charset="utf-8">
<title>TOLVANE Cabinetry Inc. – Business Card</title>
<link rel="stylesheet" href="https://fonts.googleapis.com/css2?family=Questrial&display=swap">
<style>
  :root {
    --bg: #e4e5e7;
    --card: #ffffff;
    --ink: #5a5b5e;
    --ink-soft: #7d7e82;
    --orange: #f07d22;
    --orange-deep: #e0651a;
    --orange-light: #f7a050;
    --photo-warm: #cfc6ae;
    --photo-cool: #a9adaa;
    --wood-a: #8a4f27;
    --wood-b: #d9a06a;
  }
  * { box-sizing: border-box; margin: 0; padding: 0; }
  html, body { width: 1200px; height: 1000px; overflow: hidden; }
  body {
    background: var(--bg);
    font-family: "Questrial", "Century Gothic", sans-serif;
    color: var(--ink);
    position: relative;
  }
  .card {
    position: absolute;
    width: 600px;
    height: 343px;
    background: var(--card);
    border-radius: 22px;
    overflow: hidden;
    box-shadow: 0 14px 30px rgba(0,0,0,.18);
  }
  .card--front { left: 60px; top: 150px; }
  .card--back  { left: 540px; top: 520px; }

  /* Company name */
  .brand {
    position: absolute;
    display: flex; align-items: center; gap: 12px;
    color: var(--ink); line-height: 1; white-space: nowrap;
  }
  .brand__mark { flex: none; background: var(--orange); }
  .card--front .brand { left: 36px; top: 66px; font-size: 32px; letter-spacing: 2px; }
  .card--front .brand__mark { width: 16px; height: 16px; }
  .card--back .brand { left: 30px; top: 58px; font-size: 17px; letter-spacing: 1px; gap: 9px; }
  .card--back .brand__mark { width: 11px; height: 11px; }

  /* Front */
  .photo-strip {
    position: absolute; left: 0; right: 0; top: 150px; height: 140px;
    background: linear-gradient(90deg, var(--photo-warm) 0%, #e6e0cf 35%, var(--photo-cool) 65%, #cbc8b6 100%);
  }
  .portfolio {
    position: absolute; right: 28px; top: 300px;
    font-size: 16px; color: var(--ink-soft);
  }
  .portfolio a { color: var(--orange); text-decoration: none; }
  .phone-pill {
    position: absolute; left: 30px; top: 268px;
    height: 52px; padding: 0 24px 0 16px;
    display: flex; align-items: center; gap: 14px;
    background: linear-gradient(180deg, var(--orange-light), var(--orange));
    border-radius: 14px; color: #fff; font-size: 24px; letter-spacing: 1px;
  }
  .phone-pill__icon {
    width: 30px; height: 30px; background: #fff; border-radius: 6px;
    display: flex; align-items: center; justify-content: center;
  }

  /* Back */
  .contact {
    position: absolute; left: 320px; top: 30px;
    font-size: 13px; color: var(--ink-soft); line-height: 1.35;
  }
  .contact__phone { color: var(--orange); font-size: 17px; letter-spacing: 1px; margin-bottom: 6px; }
  .contact__email { margin-top: 10px; }
  .services-band {
    position: absolute; left: 0; right: 0; top: 145px; bottom: 0;
    background: linear-gradient(135deg, var(--orange-light), var(--orange) 55%, var(--orange-deep));
  }
  .feature-photo {
    position: absolute; left: 0; top: 0; bottom: 0; width: 240px;
    background: linear-gradient(160deg, #efe9df 0%, var(--wood-b) 45%, var(--wood-a) 100%);
  }
  .services {
    position: absolute; left: 258px; top: 10px; right: 20px;
    list-style: none; color: #fff; font-size: 14px; line-height: 19.5px;
  }
  .services li::before {
    content: ""; display: inline-block; width: 5px; height: 5px;
    background: #fff; border-radius: 50%; margin: 0 10px 2px 0; vertical-align: middle;
  }
</style>
</head>
<body>

  <section class="card card--front" aria-label="Card front">
    <div class="brand"><span class="brand__mark"></span>TOLVANE CABINETRY INC.</div>
    <div class="photo-strip" role="img" aria-label="Strip of photographs of finished kitchens and bathrooms with cream cabinetry"></div>
    <p class="portfolio">Portfolio at: <a>TOLVANEcabinetry.example</a></p>
    <div class="phone-pill">
      <span class="phone-pill__icon">
        <svg width="18" height="18" viewBox="0 0 24 24" aria-hidden="true">
          <path fill="#f07d22" d="M6.6 10.8a15 15 0 0 0 6.6 6.6l2.2-2.2a1 1 0 0 1 1-.25 11.4 11.4 0 0 0 3.6.57 1 1 0 0 1 1 1V20a1 1 0 0 1-1 1A17 17 0 0 1 3 4a1 1 0 0 1 1-1h3.5a1 1 0 0 1 1 1c0 1.25.2 2.45.57 3.57a1 1 0 0 1-.25 1z"/>
        </svg>
      </span>
      555-271-4486
    </div>
  </section>

  <section class="card card--back" aria-label="Card back">
    <div class="brand"><span class="brand__mark"></span>TOLVANE CABINETRY INC.</div>
    <div class="contact">
      <div class="contact__phone">555-271-4486</div>
      <div>2290 Harbor Mill rd,</div>
      <div>Eastbrook, NY, 11900</div>
      <div class="contact__email">orin@tolvane-mail.example</div>
    </div>
    <div class="services-band">
      <div class="feature-photo" role="img" aria-label="Photograph of a curved wooden slatted stair enclosure in a modern interior"></div>
      <ul class="services">
        <li>Design and Planning</li>
        <li>Detailed Shop Drawing and Changes</li>
        <li>Full Selection of Custom Moldings</li>
        <li>Custom Entry and Interior Doors</li>
        <li>Custom Screened Doors</li>
        <li>Wood Counter, Any Wood Species</li>
        <li>Custom Elegant window Shutters</li>
        <li>Wood Beams, any size, any species</li>
        <li>We Install Our Own Cabinetry</li>
      </ul>
    </div>
  </section>

</body>
</html>
```